Fitness competition business needs a card design

I need a professional business card design using my logo. The card will be horizontal with rounded edges.

Target Market(s)

Female fitness competitors

Industry/Entity Type

Fitness

Contact Information for Business Card

Rose-Lynn Darby
Owner
stagevarno.com
555.301.2187
info@stagevarno.com

Font styles to use
Serif

Colors

Designer to choose colors to be used in the design.

Requirements
Must have
• On the back please add the following:
• Figure
• Bikini
• Physique
• Fitness
Nice to have
• Looking for a very sleek design, contemporary and easy to read.
Should not have
• Should not be difficult to read or be too busy

```html
<!DOCTYPE html>
<html lang="en">
<head>
<meta charset="utf-8">
<title>Stage Varno – Business Card</title>
<link rel="stylesheet" href="https://fonts.googleapis.com/css2?family=Roboto+Slab:wght@400;500;700&display=swap">
<style>
  :root {
    --brand-red: #e3202c;
    --brand-red-dark: #c9161f;
    --ink-grey: #4a4a4a;
    --soft-grey: #666666;
    --card-white: #f6f6f6;
    --backdrop: #e4e4e6;
  }
  * { box-sizing: border-box; margin: 0; padding: 0; }
  html, body {
    width: 1200px; height: 960px; overflow: hidden;
    background: var(--backdrop);
    font-family: "Roboto Slab", Georgia, serif;
  }
  .stage { position: relative; width: 1200px; height: 960px; }

  .card {
    position: absolute;
    width: 630px; height: 360px;
    border-radius: 18px;
    overflow: hidden;
    box-shadow: 0 10px 28px rgba(0,0,0,0.18);
  }

  /* Back side */
  .card-back {
    left: 450px; top: 90px;
    background: linear-gradient(135deg, var(--brand-red) 0%, var(--brand-red-dark) 100%);
    color: #fff;
  }
  .card-back .watermark-circle {
    position: absolute; left: 40px; top: 40px;
    width: 280px; height: 280px; border-radius: 50%;
    background: rgba(255,255,255,0.08);
  }
  .card-back .division-list {
    position: absolute; right: 40px; top: 40px;
    list-style: none; text-align: right;
  }
  .card-back .division-list li {
    font-size: 16px; font-weight: 500; letter-spacing: 3px;
    text-transform: uppercase; line-height: 28px; color: #fff;
  }
  .card-back .back-brand {
    position: absolute; right: 40px; bottom: 72px;
    font-weight: 700; font-size: 38px; letter-spacing: 1px;
    text-transform: uppercase; color: #fff;
  }
  .card-back .back-rule {
    position: absolute; right: 40px; bottom: 62px;
    width: 258px; height: 2px; background: rgba(255,255,255,0.85);
  }
  .card-back .back-url {
    position: absolute; right: 40px; bottom: 34px;
    font-size: 15px; letter-spacing: 2.5px; color: #fff;
  }

  /* Front side */
  .card-front {
    left: 130px; top: 500px;
    background: var(--card-white);
  }
  .front-brand {
    position: absolute; left: 44px; top: 52px;
    display: flex; align-items: center; gap: 12px;
  }
  .front-brand .brand-square {
    width: 22px; height: 22px; background: var(--ink-grey);
  }
  .front-brand .brand-name {
    font-weight: 700; font-size: 34px; text-transform: uppercase;
    color: var(--brand-red); letter-spacing: 0.5px;
  }

  .contact-block {
    position: absolute; right: 36px; bottom: 36px; width: 280px;
  }
  .person-name {
    font-weight: 700; font-size: 21px; color: var(--brand-red);
    text-transform: uppercase; letter-spacing: 0.3px; white-space: nowrap;
  }
  .person-role {
    font-size: 14px; color: var(--ink-grey); text-transform: uppercase;
    margin-top: 2px; padding-bottom: 8px;
    border-bottom: 2px solid var(--brand-red);
  }
  .contact-list { list-style: none; margin-top: 10px; }
  .contact-list li {
    display: flex; align-items: center; gap: 10px;
    font-size: 15px; color: var(--soft-grey); line-height: 24px; white-space: nowrap;
  }
  .contact-list svg { width: 14px; height: 14px; fill: var(--brand-red); flex: none; }
</style>
</head>
<body>
<main class="stage">

  <section class="card card-back" aria-label="Card back">
    <div class="watermark-circle"></div>
    <ul class="division-list">
      <li>Figure</li>
      <li>Bikini</li>
      <li>Physique</li>
      <li>Fitness</li>
    </ul>
    <div class="back-brand">Stage Varno</div>
    <div class="back-rule"></div>
    <div class="back-url">www.stagevarno.com</div>
  </section>

  <section class="card card-front" aria-label="Card front">
    <div class="front-brand">
      <span class="brand-square"></span>
      <span class="brand-name">Stage Varno</span>
    </div>

    <div class="contact-block">
      <div class="person-name">Rose-Lynn Darby</div>
      <div class="person-role">Owner</div>
      <ul class="contact-list">
        <li>
          <svg viewBox="0 0 24 24" aria-hidden="true"><path d="M6.6 10.8a15.1 15.1 0 0 0 6.6 6.6l2.2-2.2a1 1 0 0 1 1-.25 11.4 11.4 0 0 0 3.6.57 1 1 0 0 1 1 1V20a1 1 0 0 1-1 1A17 17 0 0 1 3 4a1 1 0 0 1 1-1h3.5a1 1 0 0 1 1 1c0 1.25.2 2.45.57 3.57a1 1 0 0 1-.25 1z"/></svg>
          555.301.2187
        </li>
        <li>
          <svg viewBox="0 0 24 24" aria-hidden="true"><path d="M2 5h20v2l-10 7L2 7z M2 8.5l10 7 10-7V19H2z"/></svg>
          info@stagevarno.com
        </li>
        <li>
          <svg viewBox="0 0 24 24" aria-hidden="true"><circle cx="12" cy="12" r="10"/><path d="M2 12h20M12 2c3 3 3 17 0 20M12 2c-3 3-3 17 0 20" stroke="#fff" stroke-width="1.4" fill="none"/></svg>
          stagevarno.com
        </li>
      </ul>
    </div>
  </section>

</main>
</body>
</html>
```